We need a single web page design for a promotion. This page will acts as a landing page for users. Please provide us with a cutting edge design. I have attached a previous design used a couple of years ago.

Link: http://www.brightleafsnaps.com/bonuspack/
Updates

The Start Here box needs to look like this:

-Start Here (heading) 
-A box for email addresses to be entered
-Then a check box with "Yes, I have read and agree to the Privacy Policy and agree to receive email marketing from Bright Leaf Snaps and acknowledge that I will receive special email offers from our marketing partners, including the Ledger Post newsletter."
-A submit button 

All of this information needs to be in one box please.  And please feel free to contact me if you have any questions about this. 

Target Market(s)

Middle aged women (housewives)

Requirements
Must have
• Images must reflect the "500 Photo Prints". The only fields that are necessary are a box for email and a submit button.
Should not have
• The word FREE anywhere on the page

```html
<!DOCTYPE html>
<html lang="en">
<head>
<meta charset="utf-8">
<title>Bright Leaf Snaps – 500 Photo Prints</title>
<link rel="stylesheet" href="https://fonts.googleapis.com/css2?family=Poppins:wght@300;600&family=Roboto+Condensed:wght@700&family=Arimo:wght@400;700&display=swap">
<style>
  :root {
    --bg-edge: #f1d3ec;
    --bg-center: #fdf6fc;
    --pink: #e57ad0;
    --pink-deep: #c94fb3;
    --pink-soft: #f3b4e6;
    --label: #b04a9d;
    --ink: #6b6b6b;
    --fine: #8a8a8a;
    --panel-top: #ffffff;
    --panel-bottom: #e4e4e4;
    --frame: #ffffff;
    --field: #f1f1f1;
    --field-line: #cfcfcf;
    --logo: #3b9be0;
  }
  * { box-sizing: border-box; margin: 0; padding: 0; }
  html, body { width: 1200px; height: 880px; overflow: hidden; }
  body {
    background: radial-gradient(ellipse 70% 65% at 50% 45%, var(--bg-center) 0%, #f9e8f6 55%, var(--bg-edge) 100%);
    font-family: "Arimo", Arial, sans-serif;
    position: relative;
  }
  .headline {
    position: absolute; top: 58px; left: 0; width: 100%;
    text-align: center;
    font-family: "Poppins", sans-serif;
    font-size: 43px; letter-spacing: -1px; line-height: 1.2;
    color: var(--pink);
    white-space: nowrap;
  }
  .headline .light { font-weight: 300; }
  .headline .strong { font-weight: 600; color: var(--pink-deep); }

  .collage { position: absolute; left: 160px; top: 135px; width: 840px; height: 460px; }
  .print {
    position: absolute;
    border: 9px solid var(--frame);
    box-shadow: 0 4px 10px rgba(120, 60, 110, 0.28);
  }
  .print.back { background: linear-gradient(160deg, #fbfbfb, #e6e9ec); }
  .print.kids { background: linear-gradient(150deg, #f2ede7, #d8b48e 60%, #6d6f8f); }
  .print.couple { background: linear-gradient(160deg, #eef1ee, #d9b898 45%, #7fb59c 75%, #c9a27c); }
  .print.mother { background: linear-gradient(170deg, #f1efe9, #e7c8aa 40%, #f4f2ef 75%, #b88d5e); }
  .print.boy { background: linear-gradient(165deg, #f0eee8, #d8b896 45%, #c7d7ea 80%, #9a7a52); }

  .signup {
    position: absolute; left: 348px; top: 465px; width: 501px; height: 255px;
    border-radius: 12px;
    background: linear-gradient(var(--panel-top), var(--panel-bottom));
    box-shadow: 0 3px 12px rgba(0, 0, 0, 0.22);
    text-align: center;
  }
  .signup-title {
    margin-top: 8px;
    font-family: "Roboto Condensed", sans-serif;
    font-size: 42px; font-weight: 700; letter-spacing: 0.5px; line-height: 1.1;
    color: var(--pink);
  }
  .email-row { display: flex; align-items: center; justify-content: center; gap: 22px; margin-top: 6px; }
  .email-row label { font-size: 14px; font-weight: 700; color: var(--label); white-space: nowrap; }
  .email-row input {
    width: 262px; height: 29px;
    background: var(--field); border: 1px solid var(--field-line); border-radius: 3px;
  }
  .consent { display: flex; gap: 8px; width: 460px; margin: 12px auto 0; text-align: left; }
  .consent input { width: 10px; height: 10px; margin-top: 1px; flex: none; }
  .consent p { font-size: 9px; line-height: 1.35; color: var(--ink); }
  .consent a { color: var(--ink); }
  .submit {
    display: block; margin: 12px auto 0; width: 102px; height: 32px;
    border: none; border-radius: 16px;
    background: linear-gradient(var(--pink-soft), var(--pink-deep));
    color: #fff; font-family: "Arimo", sans-serif; font-size: 17px; font-weight: 700;
  }
  .benefits { margin-top: 10px; font-size: 13.5px; font-weight: 700; color: var(--pink); white-space: nowrap; }
  .benefits span { margin: 0 4px; }
  .brand { display: flex; align-items: center; justify-content: center; gap: 6px; margin-top: 8px; }
  .brand .mark { width: 13px; height: 13px; background: var(--logo); }
  .brand .name { font-size: 12px; font-weight: 700; color: var(--logo); }

  .terms {
    position: absolute; left: 205px; top: 762px; width: 790px;
    text-align: center; font-size: 8.5px; line-height: 1.3; color: var(--fine);
  }
  .terms p + p { margin-top: 8px; }
  .terms p:first-child { margin-bottom: 12px; }
</style>
</head>
<body>
  <h1 class="headline"><span class="light">Get 500 Photo Prints </span><span class="strong">Delivered To You</span></h1>

  <div class="collage">
    <div class="print back" style="left:25px;top:0;width:170px;height:180px;transform:rotate(9deg)" role="img" aria-label="Photo print of a bright living room"></div>
    <div class="print back" style="left:520px;top:-10px;width:150px;height:150px;transform:rotate(-12deg)" role="img" aria-label="Photo print of a bright window"></div>
    <div class="print back" style="left:620px;top:25px;width:140px;height:150px;transform:rotate(14deg)" role="img" aria-label="Photo print of a bright room"></div>
    <div class="print kids" style="left:0;top:165px;width:190px;height:200px;transform:rotate(-22deg)" role="img" aria-label="Photo print of a girl playing on the sofa"></div>
    <div class="print couple" style="left:90px;top:20px;width:300px;height:330px;transform:rotate(-6deg)" role="img" aria-label="Photo print of a laughing family on the sofa"></div>
    <div class="print mother" style="left:350px;top:30px;width:250px;height:300px;transform:rotate(5deg)" role="img" aria-label="Photo print of a smiling mother"></div>
    <div class="print boy" style="left:580px;top:75px;width:220px;height:270px;transform:rotate(9deg)" role="img" aria-label="Photo print of a boy taking pictures with a camera"></div>
  </div>

  <form class="signup">
    <h2 class="signup-title">START HERE</h2>
    <div class="email-row">
      <label for="email">Enter your Email Address</label>
      <input id="email" type="email">
    </div>
    <div class="consent">
      <input type="checkbox" id="agree">
      <p>YES, I have read and agree to the <a href="#">Privacy Policy</a> and agree to receive email marketing from Bright Leaf Snaps and acknowledge that I will receive special email offers from our marketing partners, including the Ledger Post newsletter.</p>
    </div>
    <button class="submit" type="button">Submit</button>
    <div class="benefits">Professional Quality Photos<span>|</span>Unlimited Storage<span>|</span>Share With Your Friends</div>
    <div class="brand"><span class="mark"></span><span class="name">BrightLeafSnaps.com</span></div>
  </form>

  <div class="terms">
    <p>*OFFER REDEMPTION WILL REQUIRE PARTICIPATION AND / OR PURCHASE OF THIRD PARTY OFFERS.</p>
    <p>To receive the membership incentive gift of Five Hundred (500) photo prints you must complete all of the steps outlined herein. Prospective members must: (a) submit their zip code to determine geographic eligibility; (b) register with a valid and deliverable email address; (c) submit accurate contact and demographic information including a mailing address; (d) Accumulate a total of Twenty Five (25) points by either answering survey questions, completing lead questionnaires, or taking advantage of 3rd party offers. Purchase may be required. Please read participation requirements for details.</p>
    <p>On each page, you will be able to see your current point total and the total number of points necessary to redeem the incentive gift. Upon completion of all requirements and upload of the necessary photos, we will ship the incentive gift to you at no shipping cost. Unless otherwise indicated, participation eligibility is restricted to US residents, 18 and over. Void where prohibited.</p>
  </div>
</body>
</html>
```